Business Card for Marriage Commissioner

I am a marriage commissioner in the province of Alberta, meaning that I perform civil unions here. I have been trying to think of a unique design for my business card, something a bit different. A lot of "unique" designs seem to incorporate unique cuts or "some assembly required" or printed on plastic or meat. I would like my design to be a full colour card that is a typical business card size.

The information on the card should have:
Lou Varnik
my occupation: Marriage Commissioner
my website: www.louvarnik.ca
my e-mail: lou@louvarnik.ca
my phone: 780-418-2964

I originally submitted a design to the printer that had a screen capture of a findly search window, with my name and occupation in the text box. And underneath that, my phone number. Nothing else. They indicated they could not print this because it was a copyright violation.

One option on the design is I am a retired chemist-so a chemistry themed card would also be of interest, as long as it isn't a "Rusted Tide" theme, as I have that on my other business cards already...

I would prefer a single sided card, but I am open to a double sided card if it is clever!

I would also prefer not to have pictures of male and female couples as in my position I will also marry same sex couples. Same thing for male/female symbols. Someone has submitted two graduated cylinders in love, which is very clever, and gets around this male/female type.

Thanks for your help and interest.

Target Market(s)

Young couples.

Industry/Entity Type

Plastic

Requirements
Nice to have
• chemistry ideas!
Should not have
• Male/female pictures, male/female symbols.
No QR codes.
No transparent designs, will go on paper stock.

```html
<!DOCTYPE html>
<html lang="en">
<head>
<meta charset="utf-8">
<title>Lou Varnik – Marriage Commissioner Business Cards</title>
<link rel="stylesheet" href="https://fonts.googleapis.com/css2?family=Mulish:wght@400;700&family=Arimo:wght@400&display=swap">
<style>
  :root {
    --canvas: #e8e3dc;
    --card-dark: #232224;
    --card-mid: #3a393b;
    --red: #c01f30;
    --red-deep: #7c0a14;
    --silver-light: #e6e6e6;
    --silver-dark: #8a8a8a;
    --text-white: #ffffff;
    --text-soft: #dcdcdc;
  }
  * { box-sizing: border-box; margin: 0; padding: 0; }
  html, body { width: 1200px; height: 1000px; overflow: hidden; }
  body { background: var(--canvas); position: relative; font-family: "Arimo", Arial, sans-serif; }

  .card {
    position: absolute;
    width: 543px;
    height: 314px;
    border-radius: 26px;
    overflow: hidden;
    background: radial-gradient(ellipse at 50% 40%, var(--card-mid) 0%, var(--card-dark) 70%);
    box-shadow: 0 6px 16px rgba(0,0,0,0.35);
  }
  .card--front { left: 47px; top: 198px; height: 310px; }
  .card--back-left-top { left: 620px; top: 198px; }
  .card--back-left { left: 47px; top: 523px; }
  .card--back-center { left: 620px; top: 523px; }

  .heart-pattern {
    position: absolute;
    left: 170px; top: 0; width: 373px; height: 270px;
    background: radial-gradient(ellipse at 40% 50%, rgba(255,255,255,0.05) 0%, rgba(0,0,0,0.08) 70%);
  }

  .mark {
    position: absolute;
    display: flex; align-items: center; gap: 8px;
    font-family: "Mulish", sans-serif; font-weight: 700;
    color: var(--red);
  }
  .mark__dot { width: 12px; height: 12px; border-radius: 50%; background: var(--red); }
  .mark--large { left: 0; right: 0; top: 0; bottom: 0; justify-content: center; font-size: 54px; gap: 18px; }
  .mark--large .mark__dot { width: 30px; height: 30px; }
  .mark--small { left: 34px; top: 38px; font-size: 18px; }

  .holder { position: absolute; font-family: "Mulish", sans-serif; color: var(--text-white); }
  .holder__name { font-weight: 700; font-size: 26px; line-height: 1.1; }
  .holder__role { font-weight: 400; font-size: 16px; color: var(--text-soft); margin-top: 4px; }

  .card--back-left-top .holder { left: 32px; top: 98px; }
  .card--back-left .holder { right: 30px; top: 144px; text-align: right; }
  .card--back-center .holder { left: 0; right: 0; top: 118px; text-align: center; }
  .card--back-center .holder__role { font-size: 19px; }

  .contact { position: absolute; right: 26px; top: 202px; text-align: right; color: var(--text-white); font-size: 16px; }
  .card--back-left .contact { top: 212px; }
  .contact__line { display: flex; justify-content: flex-end; align-items: center; gap: 6px; height: 22px; }
  .contact__icon { width: 12px; height: 12px; }

  .footer-rule {
    position: absolute; left: 0; right: 0; top: 265px; height: 5px;
    background: linear-gradient(90deg, var(--silver-dark), var(--silver-light) 40%, var(--silver-light) 60%, var(--silver-dark));
  }
  .footer-band {
    position: absolute; left: 0; right: 0; top: 270px; bottom: 0;
    background: linear-gradient(90deg, var(--red-deep) 0%, var(--red) 25%, var(--red) 75%, var(--red-deep) 100%);
    display: flex; align-items: center; justify-content: center;
    color: var(--text-white); font-size: 16px;
  }
</style>
</head>
<body>

  <section class="card card--front">
    <div class="mark mark--large"><span class="mark__dot"></span>Lou Varnik</div>
  </section>

  <section class="card card--back-left-top">
    <div class="heart-pattern" role="img" aria-label="Faint repeating pattern of hearts"></div>
    <div class="mark mark--small"><span class="mark__dot"></span>Lou Varnik</div>
    <div class="holder">
      <p class="holder__name">Lou Varnik</p>
      <p class="holder__role">Marriage Commissioner</p>
    </div>
    <div class="contact">
      <p class="contact__line">780-418-2964
        <svg class="contact__icon" viewBox="0 0 12 12"><rect x="3" y="0.5" width="6" height="11" rx="1" fill="none" stroke="#c01f30" stroke-width="1.2"/></svg></p>
      <p class="contact__line">lou@louvarnik.ca
        <svg class="contact__icon" viewBox="0 0 12 12"><rect x="0.6" y="2.5" width="10.8" height="7" fill="none" stroke="#c01f30" stroke-width="1.2"/><path d="M0.6 2.5 L6 7 L11.4 2.5" fill="none" stroke="#c01f30" stroke-width="1.2"/></svg></p>
    </div>
    <div class="footer-rule"></div>
    <div class="footer-band">www.louvarnik.ca</div>
  </section>

  <section class="card card--back-left">
    <div class="heart-pattern" role="img" aria-label="Faint repeating pattern of hearts"></div>
    <div class="mark mark--small"><span class="mark__dot"></span>Lou Varnik</div>
    <div class="holder">
      <p class="holder__name">Lou Varnik</p>
      <p class="holder__role">Marriage Commissioner</p>
    </div>
    <div class="contact">
      <p class="contact__line">780-418-2964
        <svg class="contact__icon" viewBox="0 0 12 12"><rect x="3" y="0.5" width="6" height="11" rx="1" fill="none" stroke="#c01f30" stroke-width="1.2"/></svg></p>
      <p class="contact__line">lou@louvarnik.ca
        <svg class="contact__icon" viewBox="0 0 12 12"><rect x="0.6" y="2.5" width="10.8" height="7" fill="none" stroke="#c01f30" stroke-width="1.2"/><path d="M0.6 2.5 L6 7 L11.4 2.5" fill="none" stroke="#c01f30" stroke-width="1.2"/></svg></p>
    </div>
    <div class="footer-rule"></div>
    <div class="footer-band">www.louvarnik.ca</div>
  </section>

  <section class="card card--back-center">
    <div class="heart-pattern" role="img" aria-label="Faint repeating pattern of hearts"></div>
    <div class="mark mark--small"><span class="mark__dot"></span>Lou Varnik</div>
    <div class="holder">
      <p class="holder__name">Lou Varnik</p>
      <p class="holder__role">Marriage Commissioner</p>
    </div>
    <div class="contact">
      <p class="contact__line">780-418-2964
        <svg class="contact__icon" viewBox="0 0 12 12"><rect x="3" y="0.5" width="6" height="11" rx="1" fill="none" stroke="#c01f30" stroke-width="1.2"/></svg></p>
      <p class="contact__line">lou@louvarnik.ca
        <svg class="contact__icon" viewBox="0 0 12 12"><rect x="0.6" y="2.5" width="10.8" height="7" fill="none" stroke="#c01f30" stroke-width="1.2"/><path d="M0.6 2.5 L6 7 L11.4 2.5" fill="none" stroke="#c01f30" stroke-width="1.2"/></svg></p>
    </div>
    <div class="footer-rule"></div>
    <div class="footer-band">www.louvarnik.ca</div>
  </section>

</body>
</html>
```